Clotted cream packaging design (card sleeve over a plain round tub) - family owned UK business.

We require a new design for our clotted cream packaging - (a card sleeve which slips over a plain round tub - photos included to show exactly what the sleeve looks like). This will mainly involve organising the layout with a little bit of scope for some creative work. To tie the design in with our other products we will use the Bellwick Farm logo (This already exists and is attached) - there are no other requirements in regards to tying in with any other of our products. We are looking for something fairly different to our current design (can view it at www.bellwick-example.com).

We are a family owned business producing various dairy products, all of which are handcrafted from start to finish on our organic farm. We are based in North Yorkshire, England.

Our clotted cream is somewhat indulgent/luxurious, the design should subtly reflect this. I’d like it to be fairly clean/minimalistic without forgetting the fact that it is made on a working farm.
Our business is proud of the fact that we’re organic and farm in a sustainable and environmentally friendly way. The word organic needs to be prominent on the side of the sleeve.
The design should use a maximum of 4 colours with the base colour being an off white/cream colour. Our previous design included a purple which I am happy to go with again (although not completely set on it).

Must haves and where it should most likely be placed:

Top (main rounded face):

Logo: Bellwick Farm logo (attatched)
Text: ‘Yorkshire Clotted Cream’ (‘Clotted Cream’ in slightly larger font than ‘Yorkshire’)
Text: ‘113g’ (This is the product weight)

Side/s:

Text: ‘Organic’ ( prominent - both sides)
Text: 'Yorkshire Clotted Cream' (both sides)
Text: ‘Handcrafted on the farm’ (probably just on one side)
Text: ‘Perfect with puds’ (probably just on one side)

Bottom:

Image: Barcode (pdf attached)

Image: Healthmark (oval shape with GB KT482 inside - PDF Attached. Have approx 10mm wide)

Image: PC&R logo (pdf attached - please ensure the height of the PC&R logo is a minimum of 9mm. The colour of this logo can be changed to all black if it works better)

Text: Bellwick Farm, East Calmby, Northallerton, North Yorkshire, TQ9 4XR

Text: ‘All of the milk used to make our clotted cream comes from our own organic cows. Our Indulgent clotted cream is made entirely on farm, from start to finish.’

Text: Ingredients: Fresh organic milk
Allergens: milk

Image: Social media handle & web address (pdf attached)

Text: ‘Keep refrigerated. For best results leave at room temperature for 20 minutes before use.'

Target Market(s)

We predominantly sell in high-end farmshops and deli’s. Targeting people with mid to high disposable income who value the quality and provenance of their food.

Industry/Entity Type

Food

Colors
6B429C
8869AF
B7A5CE
E3DAEB
F3F0F8

Requirements
Must have
• Listed in the project description above. A clean uncluttered design
Nice to have
• Some brands that I quite like: Larkhollow Cheddar, Brunna's dairy, The Pemberly dairy, Whitlow knot cheese.
Should not have
• Not too much going on (not too busy)

```html
<!DOCTYPE html>
<html lang="en">
<head>
<meta charset="utf-8">
<title>Organic Clotted Cream – Sleeve Side Panel</title>
<link rel="stylesheet" href="https://fonts.googleapis.com/css2?family=Montserrat:wght@400;800&family=Libre+Baskerville:wght@700&display=swap">
<style>
  :root {
    --sleeve-navy: #1c1654;
    --sleeve-edge: #2a2a33;
    --type-cream: #f6f6c8;
    --canvas-bg: #efeee8;
  }
  html, body {
    margin: 0;
    padding: 0;
    overflow: hidden;
  }
  body {
    width: 1200px;
    height: 1200px;
    background: var(--canvas-bg);
    position: relative;
  }
  .sleeve-side {
    position: absolute;
    left: 80px;
    top: 266px;
    width: 1040px;
    height: 668px;
  }
  .sleeve-shape {
    position: absolute;
    inset: 0;
    width: 100%;
    height: 100%;
  }
  .sleeve-shape path {
    fill: var(--sleeve-navy);
    stroke: var(--sleeve-edge);
    stroke-width: 4;
  }
  .sleeve-text {
    position: absolute;
    left: 0;
    width: 100%;
    margin: 0;
    text-align: center;
    color: var(--type-cream);
    line-height: 1;
  }
  .sleeve-text--organic {
    top: 300px;
    font-family: "Montserrat", sans-serif;
    font-weight: 800;
    font-size: 128px;
    letter-spacing: 2px;
  }
  .sleeve-text--product {
    top: 445px;
    font-family: "Montserrat", sans-serif;
    font-weight: 400;
    font-size: 70px;
    letter-spacing: 2px;
  }
  .sleeve-text--tagline {
    top: 570px;
    font-family: "Libre Baskerville", serif;
    font-weight: 700;
    font-size: 28px;
    letter-spacing: 3px;
  }
</style>
</head>
<body>
  <section class="sleeve-side">
    <svg class="sleeve-shape" viewBox="0 0 1040 668" aria-hidden="true">
      <path d="M2 2 H317 V214 H796 V2 H1038 V666 H2 Z"/>
    </svg>
    <h1 class="sleeve-text sleeve-text--organic">ORGANIC</h1>
    <p class="sleeve-text sleeve-text--product">CLOTTED CREAM</p>
    <p class="sleeve-text sleeve-text--tagline">HANDCRAFTED ON THE FARM</p>
  </section>
</body>
</html>
```